Vireo Halden Business Cards

Vireo Halden Luxury Brand Collection is a global representation business focusing on high end luxury. We need business cards to epitomize our global, luxury delivery model.

Target Market(s)

Global Representation in the hospitality industry

Industry/Entity Type

Hospitality

Contact Information for Business Card

name
title
email: first.last@vh-kmt.com
web: www.vh-kmt.com
mobile:

Requirements
Must have
• double sided design
• incorporate logo colours
• have logo prominent
Should not have
• no designs not incorporating logo colours.

```html
<!DOCTYPE html>
<html lang="en">
<head>
<meta charset="utf-8">
<title>Vireo Halden Business Cards</title>
<link rel="stylesheet" href="https://fonts.googleapis.com/css2?family=Cinzel:wght@400;500&family=Open+Sans:wght@400&display=swap">
<style>
  :root {
    --backdrop: #2b2d31;
    --card-light: #ffffff;
    --card-dark: #1f1f20;
    --gold: #a88a52;
    --ink: #2a2a2a;
    --ink-soft: #444444;
    --url-light: #d8d8d8;
  }
  * { box-sizing: border-box; margin: 0; padding: 0; }
  html, body { width: 1200px; height: 900px; overflow: hidden; }
  body {
    background: var(--backdrop);
    position: relative;
    font-family: "Open Sans", sans-serif;
  }
  .card {
    position: absolute;
    left: 250px;
    width: 700px;
    height: 400px;
    border-radius: 28px;
    overflow: hidden;
  }
  .card--front { top: 40px; background: var(--card-light); }
  .card--back { top: 460px; background: var(--card-dark); }

  .brand-name {
    font-family: "Cinzel", serif;
    font-weight: 500;
    color: var(--gold);
    text-align: center;
    line-height: 1.15;
    white-space: nowrap;
  }
  .brand-tagline {
    display: block;
    font-size: 0.4em;
    letter-spacing: 0.1em;
    margin-top: 10px;
  }
  .card--front .brand-name {
    position: absolute;
    left: 40px;
    top: 120px;
    width: 300px;
    font-size: 34px;
  }

  .contact-block {
    position: absolute;
    left: 380px;
    top: 110px;
  }
  .person-name {
    font-family: "Cinzel", serif;
    font-weight: 400;
    font-size: 30px;
    color: var(--ink);
    letter-spacing: 0.04em;
  }
  .person-title {
    font-family: "Cinzel", serif;
    font-size: 17px;
    color: var(--gold);
    letter-spacing: 0.08em;
    margin: 4px 0 26px;
  }
  .contact-list { list-style: none; }
  .contact-list li {
    display: flex;
    align-items: center;
    gap: 12px;
    font-size: 18px;
    color: var(--ink-soft);
    margin-bottom: 10px;
  }
  .contact-list svg { width: 16px; height: 16px; flex: none; }

  .back-pattern {
    position: absolute;
    inset: 0;
    background: radial-gradient(circle at 50% 45%, #262627, var(--card-dark) 70%);
  }
  .card--back .brand-name {
    position: absolute;
    left: 0;
    right: 0;
    top: 130px;
    font-size: 48px;
  }
  .back-url {
    position: absolute;
    left: 0;
    right: 0;
    top: 290px;
    text-align: center;
    font-family: "Cinzel", serif;
    font-size: 16px;
    letter-spacing: 0.22em;
    color: var(--url-light);
  }
</style>
</head>
<body>

  <section class="card card--front">
    <div class="brand-name">Vireo Halden<span class="brand-tagline">Global Hospitality Representation</span></div>
    <div class="contact-block">
      <h1 class="person-name">YOUR NAME</h1>
      <p class="person-title">JOB TITLE</p>
      <ul class="contact-list">
        <li>
          <svg viewBox="0 0 16 16"><rect x="4" y="1" width="8" height="14" rx="1.5" fill="none" stroke="var(--gold)" stroke-width="1.5"/></svg>
          000 000 0000
        </li>
        <li>
          <svg viewBox="0 0 16 16"><rect x="1" y="3" width="14" height="10" fill="var(--gold)"/><path d="M1 3 L8 9 L15 3" fill="none" stroke="#fff" stroke-width="1.2"/></svg>
          first.last@vh-kmt.com
        </li>
        <li>
          <svg viewBox="0 0 16 16"><circle cx="8" cy="8" r="6.5" fill="none" stroke="var(--gold)" stroke-width="1.4"/><path d="M1.5 8 H14.5 M8 1.5 C4.5 5 4.5 11 8 14.5 M8 1.5 C11.5 5 11.5 11 8 14.5" fill="none" stroke="var(--gold)" stroke-width="1.1"/></svg>
          www.vh-kmt.com
        </li>
      </ul>
    </div>
  </section>

  <section class="card card--back">
    <div class="back-pattern" role="img" aria-label="Faint repeating brand pattern on dark background"></div>
    <div class="brand-name">Vireo Halden<span class="brand-tagline">Global Hospitality Representation</span></div>
    <p class="back-url">WWW.VH-KMT.COM</p>
  </section>

</body>
</html>
```